Gestaltung Deutschlandfahne
Zielgruppe
Quendal Verkäufer / Quendal Käufer
Aufgabenstellung
Gestaltung einer Deutschlandfahne.
Frei in der Gestaltung nach vorgegebener Skizze

```html
<!DOCTYPE html>
<html lang="de">
<head>
<meta charset="UTF-8">
<title>Deutschlandfahne – Respekt</title>
<link rel="stylesheet" href="https://fonts.googleapis.com/css2?family=Archivo+Black&display=swap">
<style>
  :root {
    --flag-black: #0a0a0a;
    --flag-red: #dd0000;
    --flag-red-deep: #b80000;
    --flag-gold: #e6c400;
    --flag-gold-deep: #c9a800;
    --star-gold: #e2b52a;
    --star-gold-dark: #a87d10;
    --ball-light: #f4f4f4;
    --ball-shade: #9a9a9a;
    --text-black: #050505;
  }
  * { margin: 0; padding: 0; box-sizing: border-box; }
  html, body {
    width: 1200px;
    height: 800px;
    overflow: hidden;
    background: var(--flag-black);
  }
  .flag {
    position: relative;
    width: 1200px;
    height: 800px;
    overflow: hidden;
  }
  .band { position: absolute; left: 0; width: 100%; }
  .band--black { top: 0; height: 267px; background: var(--flag-black); }
  .band--red { top: 267px; height: 266px; background: var(--flag-red); }
  .band--gold { top: 533px; height: 267px; background: var(--flag-gold); }

  .crowd {
    position: absolute;
    left: 0;
    top: 500px;
    width: 100%;
    height: 170px;
    background: linear-gradient(to bottom, rgba(230,196,0,0) 0%, var(--flag-gold) 22%, var(--flag-gold-deep) 70%, var(--flag-gold) 100%);
  }

  .stars {
    position: absolute;
    left: 415px;
    top: 120px;
    width: 330px;
    height: 110px;
  }

  .ball {
    position: absolute;
    left: 430px;
    top: 290px;
    width: 300px;
    height: 300px;
    border-radius: 50%;
    background: radial-gradient(circle at 40% 35%, var(--ball-light) 0%, #dcdcdc 60%, var(--ball-shade) 100%);
  }

  .slogan {
    position: absolute;
    left: 0;
    top: 630px;
    width: 100%;
    text-align: center;
    font-family: "Archivo Black", "Arial Black", sans-serif;
    font-size: 132px;
    line-height: 1;
    letter-spacing: 0.42em;
    padding-left: 0.42em;
    color: var(--text-black);
  }
</style>
</head>
<body>
  <main class="flag">
    <div class="band band--black"></div>
    <div class="band band--red"></div>
    <div class="band band--gold"></div>

    <div class="crowd" role="img" aria-label="Jubelnde Fan-Menge als Silhouette mit Konfetti"></div>

    <svg class="stars" viewBox="0 0 330 110" aria-label="Vier Sterne">
      <defs>
        <linearGradient id="star-fill" x1="0" y1="0" x2="1" y2="1">
          <stop offset="0" stop-color="#f6d560"/>
          <stop offset="0.5" stop-color="var(--star-gold)"/>
          <stop offset="1" stop-color="var(--star-gold-dark)"/>
        </linearGradient>
        <polygon id="star" points="0,-40 9.4,-12.9 38,-12.4 15.2,4.9 23.5,32.4 0,16 -23.5,32.4 -15.2,4.9 -38,-12.4 -9.4,-12.9"/>
      </defs>
      <use href="#star" x="45" y="68" fill="url(#star-fill)"/>
      <use href="#star" x="125" y="58" fill="url(#star-fill)"/>
      <use href="#star" x="205" y="50" fill="url(#star-fill)"/>
      <use href="#star" x="285" y="62" fill="url(#star-fill)"/>
    </svg>

    <div class="ball" role="img" aria-label="Fußball"></div>

    <h1 class="slogan">RESPEKT</h1>
  </main>
</body>
</html>
```